Business Card for Fundraising Startup

Please design and good looking business card around our logo.

Name: Dale Morrow
Phone,email, website, address

We will be presenting this card to business owners in order to get them to give us coupons.

) You sign up and create a campaign. 2) We work with local businesses to provide valuable offers. 3) You share the link and code to download the mobile app. ( 4) We handle payment processing, deal delivery, customer service, etc. 5) You login to your dashboard and review your achievements/goals. 6) We deliver your funds to you. Focusing on the "you" parts, it basically comes down to: 1) Create a campaign 2) Share the mobile app with donors 3) Get paid That seems easy enough and is low-risk, high-reward so it might be something we want to highlight on the homepage.

Industry/Entity Type

Business

Contact Information for Business Card

Looking for a fun, colorful, and modern design

Requirements
Must have
• Logo

```html
<!DOCTYPE html>
<html lang="en">
<head>
<meta charset="utf-8">
<title>Givvo Stationery Set</title>
<link href="https://fonts.googleapis.com/css2?family=Nunito:wght@400;800&display=swap" rel="stylesheet">
<style>
  :root{
    --navy:#2b3a8c;
    --navy-deep:#1f2a6e;
    --green:#2e8a3c;
    --paper:#ffffff;
    --ink:#555b66;
    --board-light:#e4e5e7;
    --board-dark:#a9abae;
  }
  *{margin:0;padding:0;box-sizing:border-box}
  html,body{width:849px;height:1200px;overflow:hidden}
  body{
    position:relative;
    font-family:"Nunito",sans-serif;
    background:radial-gradient(ellipse at 50% 45%,var(--board-light) 0%,#cfd0d2 55%,var(--board-dark) 100%);
  }
  .piece{position:absolute;background:var(--paper);box-shadow:0 2px 6px rgba(0,0,0,.25)}
  .shapes{position:absolute;left:0;top:0;width:849px;height:1200px;pointer-events:none}
  .brand{position:absolute;font-weight:800;color:var(--navy);letter-spacing:-.5px;line-height:1}
  .tagline{position:absolute;font-weight:400;color:var(--green);text-transform:uppercase;letter-spacing:.6px;line-height:1}
  .footer{position:absolute;font-size:5.5px;color:var(--ink);letter-spacing:.2px;line-height:1.3}
  .footer.on-dark{color:#fff}
  .brand.on-dark{color:#fff}
  .card-name{position:absolute;font-size:7px;font-weight:800;color:var(--navy)}
  .card-role{position:absolute;font-size:5px;color:var(--ink)}
</style>
</head>
<body>

<!-- paper pieces -->
<div class="piece" style="left:74px;top:62px;width:345px;height:481px"></div>
<div class="piece" style="left:439px;top:62px;width:342px;height:481px"></div>
<div class="piece" style="left:74px;top:566px;width:345px;height:235px"></div>
<div class="piece" style="left:74px;top:821px;width:345px;height:241px"></div>
<div class="piece" style="left:439px;top:566px;width:342px;height:490px"></div>
<div class="piece" style="left:470px;top:1073px;width:147px;height:82px"></div>
<div class="piece" style="left:628px;top:1073px;width:148px;height:82px"></div>

<svg class="shapes" viewBox="0 0 849 1200" aria-hidden="true">
  <defs>
    <symbol id="star" viewBox="-1 -1 2 2">
      <polygon points="0,-1 0.225,-0.309 0.951,-0.309 0.363,0.118 0.588,0.809 0,0.382 -0.588,0.809 -0.363,0.118 -0.951,-0.309 -0.225,-0.309"/>
    </symbol>
    <linearGradient id="band" x1="0" y1="0" x2="1" y2="0">
      <stop offset="0" stop-color="#1f2a6e"/>
      <stop offset="1" stop-color="#3a4ba6"/>
    </linearGradient>
  </defs>

  <!-- sheet A -->
  <rect x="74" y="234" width="345" height="4" fill="var(--green)"/>
  <use href="#star" x="292" y="192" width="76" height="76" fill="var(--navy)"/>

  <!-- sheet B -->
  <rect x="439" y="62" width="342" height="66" fill="url(#band)"/>
  <rect x="439" y="128" width="342" height="5" fill="var(--green)"/>
  <use href="#star" x="664" y="64" width="80" height="80" fill="#3a4ba6" stroke="#fff" stroke-width=".04"/>
  <rect x="439" y="396" width="342" height="147" fill="url(#band)"/>

  <!-- sheet C -->
  <rect x="74" y="566" width="345" height="66" fill="url(#band)"/>
  <rect x="74" y="632" width="345" height="5" fill="var(--green)"/>
  <use href="#star" x="294" y="568" width="76" height="76" fill="#3a4ba6" stroke="#fff" stroke-width=".04"/>

  <!-- sheet D -->
  <rect x="74" y="934" width="345" height="4" fill="var(--green)"/>
  <use href="#star" x="292" y="896" width="76" height="76" fill="var(--navy)"/>

  <!-- letterhead E -->
  <line x1="520" y1="612" x2="781" y2="612" stroke="#b9bcc4" stroke-width="1"/>
  <use href="#star" x="662" y="597" width="30" height="30" fill="#fff" stroke="#9aa0b8" stroke-width=".06"/>
  <rect x="439" y="1022" width="342" height="8" fill="var(--green)"/>
  <rect x="439" y="1030" width="342" height="26" fill="url(#band)"/>
  <use href="#star" x="443" y="1008" width="28" height="28" fill="#fff" stroke="var(--navy)" stroke-width=".06"/>

  <!-- card front -->
  <rect x="470" y="1073" width="147" height="40" fill="var(--green)"/>
  <rect x="470" y="1113" width="147" height="42" fill="url(#band)"/>
  <use href="#star" x="560" y="1090" width="36" height="36" fill="#3a4ba6" stroke="#fff" stroke-width=".05"/>

  <!-- card back -->
  <rect x="628" y="1143" width="148" height="4" fill="var(--green)"/>
  <rect x="628" y="1147" width="148" height="8" fill="url(#band)"/>
  <use href="#star" x="738" y="1125" width="24" height="24" fill="var(--navy)"/>
</svg>

<!-- sheet A text -->
<div class="brand" style="left:100px;top:190px;font-size:40px">Givvo</div>
<div class="tagline" style="left:102px;top:244px;font-size:6px">Raising funds through local deals</div>
<div class="footer" style="left:100px;top:512px">Phone 555 0142 · hello@givvo.org · 12 Elm Street, Springfield</div>

<!-- sheet B text -->
<div class="brand" style="left:555px;top:300px;font-size:40px">Givvo</div>
<div class="tagline" style="left:557px;top:345px;font-size:6px">Raising funds through local deals</div>
<div class="footer on-dark" style="left:470px;top:515px">Phone 555 0142 · hello@givvo.org · 12 Elm Street, Springfield</div>

<!-- sheet C text -->
<div class="brand" style="left:145px;top:680px;font-size:40px">Givvo</div>
<div class="tagline" style="left:147px;top:724px;font-size:6px">Raising funds through local deals</div>
<div class="footer" style="left:100px;top:780px">Phone 555 0142 · hello@givvo.org · 12 Elm Street, Springfield</div>

<!-- sheet D text -->
<div class="brand" style="left:100px;top:888px;font-size:40px">Givvo</div>
<div class="tagline" style="left:102px;top:944px;font-size:6px">Raising funds through local deals</div>
<div class="footer" style="left:100px;top:1040px">Phone 555 0142 · hello@givvo.org · 12 Elm Street, Springfield</div>

<!-- letterhead E text -->
<div class="brand" style="left:458px;top:596px;font-size:18px">Givvo</div>
<div class="tagline" style="left:459px;top:616px;font-size:3.5px">Raising funds through local deals</div>
<div class="footer on-dark" style="left:480px;top:1039px">Phone 555 0142 · hello@givvo.org · 12 Elm Street, Springfield</div>

<!-- card front text -->
<div class="brand on-dark" style="left:478px;top:1130px;font-size:15px">Givvo</div>

<!-- card back text -->
<div class="brand" style="left:636px;top:1080px;font-size:14px">Givvo</div>
<div class="card-name" style="left:700px;top:1084px">Dale Morrow</div>
<div class="card-role" style="left:700px;top:1094px">Partnerships Lead</div>
<div class="card-role" style="left:636px;top:1110px;line-height:1.4">555 0142 · hello@givvo.org<br>12 Elm Street, Springfield</div>

</body>
</html>
```